Webdesign für Vermietung eines Ferienhauses auf der Insel Usedom
Zielgruppe
Vermietung eines Ferienhauses auf der Insel Usedom
ZG: Urlauber im gehobenem Preissegment, die Luxus schätzen und urlauben wollen
Aufgabenstellung
- IN ADOBE PHOTOSHOP
- Bilder können hier entnommen werden: https://www.quartiro-net.example/ob-link-ansicht-reserve/index.php?portal=48127&unit=39502/index.html
- gern können Sie auch Stock-Bilder verwenden
- Der Buchungskalender /die Verfügbarkeit der freien Zeiträume soll präsent im oberen Bereich der Seite stehen
- Lumivo-Bewertungsbutton
- Es gibt kein Logo - bitte den Namenszug 'KIEFERNVILLA*****HOLMSTEDE' nutzen

```html
<!DOCTYPE html>
<html lang="de">
<head>
<meta charset="utf-8">
<title>Kiefernvilla Holmstede – Das 5* Strandhaus</title>
<link href="https://fonts.googleapis.com/css2?family=Plus+Jakarta+Sans:wght@400;500;600;700&family=Inter:wght@400;500;600&display=swap" rel="stylesheet">
<style>
:root{
  --ink:#111827;
  --text:#374151;
  --muted:#6b7280;
  --faint:#9ca3af;
  --line:#d1d5db;
  --soft:#e5e7eb;
  --range:#e5e7eb;
  --accent:#1ea0e6;
  --star:#f59e0b;
  --white:#ffffff;
}
*{box-sizing:border-box;margin:0;padding:0}
html,body{width:1200px;height:2853px;overflow:hidden;background:var(--white)}
body{position:relative;font-family:"Plus Jakarta Sans",sans-serif;color:var(--text)}
.abs{position:absolute}

/* hero */
.hero{left:0;top:0;width:1200px;height:581px;
  background:linear-gradient(180deg,#3d5f8e 0%,#7d93b4 22%,#c9d2df 45%,#e9edf2 62%,#dfe4ea 80%,#b9bec4 100%)}
.brand{left:93px;top:18px;font-family:"Plus Jakarta Sans",sans-serif;font-weight:500;font-size:22px;color:var(--white);letter-spacing:.2px}
.nav{right:94px;top:26px;display:flex;gap:28px;font-size:12.5px;color:var(--white);font-weight:500}
.dots{left:560px;top:542px;display:flex;gap:9px}
.dots span{width:6px;height:6px;border-radius:50%;background:var(--white)}
.dots span.on{background:var(--accent)}

/* content */
h2{font-family:"Inter",sans-serif;font-weight:600;color:var(--ink);font-size:25px;letter-spacing:-.2px}
.copy{font-size:13.3px;line-height:20px;color:var(--text)}
.copy b{color:var(--ink);font-weight:700}
.rating{left:93px;top:672px;display:flex;align-items:center;gap:6px;font-size:15px;color:var(--text)}
.rating u{text-underline-offset:3px}
.more{left:93px;top:996px;width:127px;height:33px;border:1px solid var(--ink);border-radius:4px;font-size:12.5px;color:var(--ink);display:flex;align-items:center;justify-content:center;gap:8px}
.rule{left:93px;width:580px;height:1px;background:var(--line)}

/* calendars */
.month-title{font-size:13.5px;color:var(--ink);text-align:center;width:280px}
.cal{display:grid;grid-template-columns:repeat(7,40px);grid-auto-rows:42.4px;font-size:13.3px;color:var(--text)}
.cal.head{font-size:11px;font-weight:600;color:var(--text);grid-auto-rows:20px}
.cal span{display:flex;align-items:center;justify-content:center}
.cal .x{color:var(--faint);text-decoration:line-through}
.cal .mid{background:var(--range)}
.cal .start{background:linear-gradient(90deg,transparent 50%,var(--range) 50%)}
.cal .end{background:linear-gradient(90deg,var(--range) 50%,transparent 50%)}
.cal .start i,.cal .end i{font-style:normal;width:40px;height:40px;border-radius:50%;background:var(--accent);color:var(--white);display:flex;align-items:center;justify-content:center}
.arrow{font-size:15px;color:var(--ink)}

.photo{left:93px;width:580px;border-radius:8px}
.pano{top:1601px;height:416px;background:linear-gradient(90deg,#c9a98a 0%,#e8ddd0 30%,#f3eee6 55%,#d9c6ae 80%,#a89478 100%)}
.map{top:2276px;height:359px;background:linear-gradient(110deg,#b8dfc4 0%,#c2e4cb 45%,#9fbdf2 62%,#9cbcf5 100%)}

/* booking card */
.card{left:760px;top:632px;width:346px;height:326px;background:var(--white);border:1px solid var(--soft);border-radius:8px;box-shadow:0 2px 8px rgba(0,0,0,.08)}
.card h3{position:absolute;left:20px;top:28px;font-family:"Inter",sans-serif;font-weight:600;font-size:16.5px;color:var(--ink)}
.field{position:absolute;left:20px;width:306px;height:35px;border:1px solid var(--line);border-radius:6px;display:flex;align-items:center;padding:0 12px;gap:8px;font-size:13.3px;color:var(--muted)}
.field.sel{justify-content:flex-end}
.book{position:absolute;left:20px;top:264px;width:306px;height:36px;background:var(--accent);border-radius:6px}

.picker{left:780px;top:794px;width:214px;height:216px;background:var(--white);border-radius:6px;box-shadow:0 4px 14px rgba(0,0,0,.16)}
.picker .ttl{position:absolute;left:21px;top:16px;font-size:11.5px;color:var(--ink);font-weight:500}
.picker .nav2{position:absolute;right:18px;top:14px;font-size:12px;color:var(--ink);display:flex;gap:18px}
.mini{position:absolute;left:14px;display:grid;grid-template-columns:repeat(7,26.6px);grid-auto-rows:26.8px;font-size:11.5px;color:var(--ink)}
.mini span{display:flex;align-items:center;justify-content:center}
.mini.head{top:42px;grid-auto-rows:16px;font-size:9.5px;color:var(--muted)}
.mini .p{color:var(--faint)}
.mini .s i{font-style:normal;width:22px;height:22px;border-radius:50%;background:var(--accent);color:var(--white);display:flex;align-items:center;justify-content:center}

.footer-rule{left:93px;top:2779px;width:1013px;height:1px;background:var(--line)}
.legal{left:93px;top:2810px;font-size:13.3px;color:var(--muted)}
.links{right:94px;top:2810px;font-size:13.3px;color:var(--muted)}
</style>
</head>
<body>

<header class="abs hero" role="img" aria-label="Foto: verschneite Straße mit reetgedeckten Strandhäusern im Winter"></header>
<div class="abs brand">Kiefernvilla Holmstede</div>
<nav class="abs nav"><span>Das 5* Strandhaus</span><span>Verfügbarkeit</span><span>Die Räumlichkeiten</span><span>Lage</span><span>Kontakt</span></nav>
<div class="abs dots"><span class="on"></span><span></span><span></span><span></span><span></span><span></span></div>

<h2 class="abs" style="left:93px;top:633px">Das 5* Strandhaus</h2>
<div class="abs rating">
  <svg width="17" height="16" viewBox="0 0 24 23"><path fill="var(--star)" d="M12 0l3.1 7.6 8.2.6-6.3 5.3 2 8-7-4.4-7 4.4 2-8L.7 8.2l8.2-.6z"/></svg>
  <u>4.8/5 (347 Reviews)</u>
</div>
<p class="abs copy" style="left:93px;top:720px;width:580px"><b>"NORVALE Küstenland"</b> in Holmstede ist eine in Mecklenburg-Vorpommern einzigartige 5-Sterne-Ferienhaus-Anlage mit 42 großzügigen, schilfrohrgedeckten Strandhäusern mit bis zu 225 m² Wohnfläche und 26 Ferienwohnungen. Grundstücke mit bis zu 3300 m² Fläche bieten viel Platz zum Wohlfühlen. Dieses exklusive, 2017 erbaute Strandhaus mit ca. 145 m² Wohnfläche und einem Grundstück von ca. 700 m² befindet sich ca. 5 Gehminuten vom Strand entfernt. Das Haus verfügt über beheizbarer Aussenwhirlpool (ganzjährig nutzbar), Safe, Internet - WLAN, Sauna mit Infrarot, 2 Terrassen, HWR mit Waschmaschine und Trockner, Bollerwagen, Parkplatz.</p>
<p class="abs copy" style="left:93px;top:894px">-</p>
<p class="abs copy" style="left:93px;top:927px">Auch Langzeiturlauber sind in den Monaten November bis März herzlich willkommen!</p>
<p class="abs copy" style="left:93px;top:960px">Gerne unterbreiten wir Ihnen ein passendes Angebot mit günstigen Sondertarifen.</p>
<div class="abs more">Mehr erfahren <svg width="11" height="7" viewBox="0 0 11 7"><path d="M1 1l4.5 4.5L10 1" fill="none" stroke="var(--ink)" stroke-width="1.5"/></svg></div>
<div class="abs rule" style="top:1068px"></div>

<h2 class="abs" style="left:93px;top:1110px">Verfügbarkeit</h2>
<span class="abs arrow" style="left:104px;top:1178px">‹</span>
<div class="abs month-title" style="left:93px;top:1180px">November 2022</div>
<div class="abs month-title" style="left:393px;top:1180px">December 2022</div>
<span class="abs arrow" style="left:652px;top:1178px">›</span>

<div class="abs cal head" style="left:93px;top:1220px"><span>Su</span><span>Mo</span><span>Tu</span><span>We</span><span>Th</span><span>Fr</span><span>Sa</span></div>
<div class="abs cal" style="left:93px;top:1251px">
  <span></span><span>1</span><span>2</span><span>3</span><span>4</span><span>5</span><span>6</span>
  <span>7</span><span>8</span><span>9</span><span class="x">10</span><span class="x">11</span><span class="x">12</span><span class="x">13</span>
  <span class="x">14</span><span class="x">15</span><span>16</span><span class="start"><i>17</i></span><span class="mid">18</span><span class="mid">19</span><span class="end"><i>20</i></span>
  <span>21</span><span>22</span><span>23</span><span>24</span><span>25</span><span>26</span><span>27</span>
  <span>28</span><span>29</span><span>30</span>
</div>

<div class="abs cal head" style="left:393px;top:1220px"><span>Su</span><span>Mo</span><span>Tu</span><span>We</span><span>Th</span><span>Fr</span><span>Sa</span></div>
<div class="abs cal" style="left:393px;top:1251px">
  <span></span><span>1</span><span class="x">2</span><span>3</span><span>4</span><span>5</span><span>6</span>
  <span>5</span><span>6</span><span class="x">7</span><span>8</span><span class="x">9</span><span>10</span><span>11</span>
  <span>12</span><span>13</span><span>14</span><span>15</span><span>16</span><span>17</span><span>18</span>
  <span>19</span><span class="x">20</span><span>21</span><span>22</span><span class="x">23</span><span>24</span><span>25</span>
  <span>26</span><span>27</span><span>28</span><span>29</span><span>30</span><span>31</span>
</div>
<div class="abs rule" style="top:1501px"></div>

<h2 class="abs" style="left:93px;top:1544px">Die Räumlichkeiten</h2>
<div class="abs photo pano" role="img" aria-label="360°-Panorama: Badezimmer mit Dusche und Ruheraum mit zwei Liegestühlen"></div>
<div class="abs rule" style="top:2056px"></div>

<h2 class="abs" style="left:93px;top:2099px">Lage</h2>
<p class="abs copy" style="left:93px;top:2149px;width:580px"><b>"NORVALE Küstenland"</b> in Holmstede ist eine in Mecklenburg-Vorpommern einzigartige 5-Sterne-Ferienhaus-Anlage mit 42 großzügigen, schilfrohrgedeckten Strandhäusern mit bis zu 225 m² Wohnfläche und 26 Ferienwohnungen. Dieses exklusive, 2017 erbaute Strandhaus mit ca. 145 m² Wohnfläche und einem Grundstück von ca. 700 m² befindet sich ca. 5 Gehminuten vom Strand entfernt.</p>
<div class="abs photo map" role="img" aria-label="Karte: Lage des Strandhauses an der Küste mit Strand und Ortschaften in der Umgebung"></div>

<aside class="abs card">
  <h3>Verfügbarkeit prüfen</h3>
  <div class="field" style="top:64px"><svg width="14" height="14" viewBox="0 0 16 16"><rect x="1.5" y="2.5" width="13" height="12" rx="2" fill="none" stroke="var(--muted)" stroke-width="1.3"/><path d="M1.5 6.5h13M5 1v3M11 1v3" stroke="var(--muted)" stroke-width="1.3"/></svg>Check-In</div>
  <div class="field" style="top:113px"><svg width="14" height="14" viewBox="0 0 16 16"><rect x="1.5" y="2.5" width="13" height="12" rx="2" fill="none" stroke="var(--muted)" stroke-width="1.3"/><path d="M1.5 6.5h13M5 1v3M11 1v3" stroke="var(--muted)" stroke-width="1.3"/></svg>19. 11. 2022</div>
  <div class="field sel" style="top:164px"><svg width="12" height="8" viewBox="0 0 12 8"><path d="M1 1.5l5 5 5-5" fill="none" stroke="var(--text)" stroke-width="1.4"/></svg></div>
  <div class="field sel" style="top:214px"><svg width="12" height="8" viewBox="0 0 12 8"><path d="M1 1.5l5 5 5-5" fill="none" stroke="var(--text)" stroke-width="1.4"/></svg></div>
  <div class="book"></div>
</aside>

<div class="abs picker">
  <div class="ttl">November 2022 ˅</div>
  <div class="nav2"><span>‹</span><span>›</span></div>
  <div class="mini head"><span>Mo</span><span>Tu</span><span>We</span><span>Th</span><span>Fr</span><span>Sa</span><span>Su</span></div>
  <div class="mini" style="top:69px">
    <span></span><span></span><span></span><span class="p">1</span><span class="p">2</span><span class="p">3</span><span class="p">4</span>
    <span class="p">5</span><span class="p">6</span><span class="p">7</span><span class="p">8</span><span class="p">9</span><span class="p">10</span><span>11</span>
    <span>12</span><span>13</span><span>14</span><span>15</span><span>16</span><span>17</span><span>18</span>
    <span class="s"><i>19</i></span><span>20</span><span>21</span><span>22</span><span>23</span><span>24</span><span>25</span>
    <span>26</span><span>27</span><span>28</span><span>29</span><span>30</span>
  </div>
</div>

<div class="abs footer-rule"></div>
<div class="abs legal">© Kiefernvilla Holmstede. Alle Rechte vorbehalten.</div>
<div class="abs links">Impressum | Datenschutz</div>

</body>
</html>
```